Laura Brennick - Powerpoint slides

I am an educator and lecturer - I use powerpoint slides for my presentations. I would like to use my current logo and branding to create personalised powerpoint presentations.

I need a file with so I can select my personalized Powerpoint slides: I would like 3 colour variations of the following slides (design and layout is the same for all colours, with just the colour shades change)
1. Title Slide
2. Title & Content
3. Section Header
4. 2 content slide
5. Blank Slide

Note on colours: 3+ variations would be great - suggest background colours to be Turqoise
Dark/Grey Charcoal \
White
PLUS one free choice colour scheme from the designers.

Target Market(s)

Physiotherapists
Yoga Teachers
Students (yoga students and physiotherapy students)
Medical Professionals

Industry/Entity Type

Health And Wellness

Font styles to use
Serif
Sans Serif

Colors
33b8a4
876aae
0255a3

Requirements
Must have
• See the slide types in the brief description.
• Each slide should stay pretty much in the same colour, just different intensity of the shade.
• Please use the designs from my uploaded files.
• 3+ different colour variations for the regular content for slides
Nice to have
• Background patterns over part of the screen.
Should not have
• Not too many colour variations - I have chosen the ones I like as examples.

```html
<!DOCTYPE html>
<html lang="en">
<head>
<meta charset="utf-8">
<title>Laura Brennick – Presentation Slide Set</title>
<link href="https://fonts.googleapis.com/css2?family=Poiret+One&family=Lato:wght@300;400;700&display=swap" rel="stylesheet">
<style>
  :root {
    --teal: #1f8b81;
    --teal-light: #5fc2b5;
    --purple: #876aae;
    --purple-light: #ad96cc;
    --blue: #0d56a2;
    --blue-light: #4f8fcf;
    --white: #ffffff;
    --page: #ffffff;
    --ink: #3d4a4a;
    --muted: #8a9696;
    --thin-font: "Poiret One", "Lato", sans-serif;
    --body-font: "Lato", "Helvetica Neue", sans-serif;
  }
  * { box-sizing: border-box; margin: 0; padding: 0; }
  html, body { width: 1200px; height: 3600px; overflow: hidden; }
  body { background: var(--page); position: relative; font-family: var(--body-font); }

  .slide {
    position: absolute;
    left: 264px;
    width: 672px;
    height: 379px;
    overflow: hidden;
    box-shadow: 0 4px 10px rgba(0,0,0,0.35);
  }
  .slide--teal { background: var(--teal); --accent-light: var(--teal-light); }
  .slide--purple { background: var(--purple); --accent-light: var(--purple-light); }
  .slide--blue { background: var(--blue); --accent-light: var(--blue-light); }
  .slide--white { background: var(--white); }

  /* brand name lockup */
  .brand {
    position: absolute;
    top: 48px;
    display: flex;
    align-items: center;
    gap: 7px;
    font-family: var(--thin-font);
    font-size: 24px;
    color: var(--white);
  }
  .brand__dot { width: 16px; height: 16px; border-radius: 50%; border: 1.5px solid currentColor; }
  .brand--left { left: 24px; }
  .brand--right { right: 26px; }
  .slide--white .brand { top: 18px; color: var(--teal); font-size: 22px; }

  /* faint ornament area */
  .ornament {
    position: absolute;
    top: 0;
    height: 100%;
    width: 216px;
    opacity: 0.55;
  }
  .ornament--right { right: 0; background: radial-gradient(ellipse 70% 48% at 90% 50%, var(--accent-light), transparent 75%); }
  .ornament--left { left: 0; background: radial-gradient(ellipse 70% 48% at 10% 50%, var(--accent-light), transparent 75%); }
  .ornament--soft {
    right: 0; top: 110px; height: 240px; width: 260px; opacity: 1;
    background: radial-gradient(ellipse 55% 50% at 65% 60%, rgba(95,194,181,0.18), transparent 75%);
  }

  .title-block { position: absolute; top: 236px; color: var(--white); }
  .title-block--left { left: 29px; text-align: left; }
  .title-block--right { right: 24px; text-align: right; }
  .title-block__title { font-family: var(--thin-font); font-size: 35px; font-weight: 400; letter-spacing: 0.3px; }
  .title-block__subtitle { font-size: 9.5px; font-weight: 300; margin-top: 6px; }

  /* content slides */
  .slide-heading {
    position: absolute; left: 20px; top: 18px;
    font-family: var(--thin-font); font-size: 27px; font-weight: 400; color: var(--teal);
  }
  .slide-heading::after {
    content: ""; position: absolute; left: 0; top: 40px; width: 40px; height: 3px; background: var(--teal);
  }
  .footer-band {
    position: absolute; left: 0; bottom: 0; width: 100%; height: 19px;
    background: var(--teal); color: var(--white);
    display: flex; align-items: center; justify-content: space-between;
    padding: 0 8px 0 18px; font-size: 7px;
  }
  .footer-band__page {
    width: 18px; height: 13px; background: var(--white); color: var(--teal);
    display: flex; align-items: center; justify-content: center; font-size: 7px;
  }

  .feature-band {
    position: absolute; left: 0; top: 91px; width: 100%; height: 137px;
    background: linear-gradient(180deg, #2f9e92 0%, #1f8379 60%, #16706a 100%);
  }
  .feature {
    position: absolute; top: 118px; width: 200px; text-align: center;
  }
  .feature__photo {
    width: 96px; height: 96px; border-radius: 50%; margin: 0 auto;
    border: 2px solid rgba(255,255,255,0.7);
  }
  .feature__photo--one { background: radial-gradient(circle at 50% 40%, #9fc9d6, #4d7f8c 70%, #3b5e5a); }
  .feature__photo--two { background: linear-gradient(180deg, #f1b85a 0%, #e08a3c 45%, #2d5c7a 75%, #1d3a4f 100%); }
  .feature__photo--three { background: radial-gradient(circle at 50% 55%, #e59aa6, #a35868 55%, #6a4a4e 100%); }
  .feature__heading { margin-top: 38px; font-size: 12px; color: var(--teal); }
  .feature__text { margin: 6px auto 0; width: 170px; font-size: 8px; line-height: 1.45; color: var(--muted); }

  .photo-left {
    position: absolute; left: 24px; top: 89px; width: 300px; height: 216px;
    background: linear-gradient(180deg, #9fa6ac 0%, #d9c9a8 35%, #f6e4b8 48%, #8f7b61 62%, #3c3630 100%);
  }
  .point-list { position: absolute; left: 362px; top: 92px; width: 280px; list-style: none; }
  .point-list__item { position: relative; padding-left: 10px; margin-bottom: 27px; font-size: 8px; line-height: 1.5; color: var(--muted); }
  .point-list__item::before {
    content: ""; position: absolute; left: 0; top: 4px; width: 4px; height: 4px; border-radius: 50%; background: var(--teal);
  }
  .point-list__title { font-weight: 700; color: var(--teal); }
</style>
</head>
<body>

  <!-- title slides, ornament right -->
  <section class="slide slide--teal" style="top:12px">
    <div class="ornament ornament--right" role="img" aria-label="Faint lotus line ornament"></div>
    <div class="brand brand--left"><span class="brand__dot"></span>Laura</div>
    <div class="title-block title-block--left">
      <h1 class="title-block__title">Your Title Goes Here</h1>
      <p class="title-block__subtitle">Your Subtitle Goes Here</p>
    </div>
  </section>

  <section class="slide slide--purple" style="top:410px">
    <div class="ornament ornament--right" role="img" aria-label="Faint lotus line ornament"></div>
    <div class="brand brand--left"><span class="brand__dot"></span>Laura</div>
    <div class="title-block title-block--left">
      <h1 class="title-block__title">Your Title Goes Here</h1>
      <p class="title-block__subtitle">Your Subtitle Goes Here</p>
    </div>
  </section>

  <section class="slide slide--blue" style="top:809px">
    <div class="ornament ornament--right" role="img" aria-label="Faint lotus line ornament"></div>
    <div class="brand brand--left"><span class="brand__dot"></span>Laura</div>
    <div class="title-block title-block--left">
      <h1 class="title-block__title">Your Title Goes Here</h1>
      <p class="title-block__subtitle">Your Subtitle Goes Here</p>
    </div>
  </section>

  <!-- section slides, ornament left -->
  <section class="slide slide--teal" style="top:1207px">
    <div class="ornament ornament--left" role="img" aria-label="Faint lotus line ornament"></div>
    <div class="brand brand--right"><span class="brand__dot"></span>Laura</div>
    <div class="title-block title-block--right">
      <h1 class="title-block__title">Your Title Goes Here</h1>
      <p class="title-block__subtitle">Your Subtitle Goes Here</p>
    </div>
  </section>

  <section class="slide slide--purple" style="top:1606px">
    <div class="ornament ornament--left" role="img" aria-label="Faint lotus line ornament"></div>
    <div class="brand brand--right"><span class="brand__dot"></span>Laura</div>
    <div class="title-block title-block--right">
      <h1 class="title-block__title">Your Title Goes Here</h1>
      <p class="title-block__subtitle">Your Subtitle Goes Here</p>
    </div>
  </section>

  <section class="slide slide--blue" style="top:2004px">
    <div class="ornament ornament--left" role="img" aria-label="Faint lotus line ornament"></div>
    <div class="brand brand--right"><span class="brand__dot"></span>Laura</div>
    <div class="title-block title-block--right">
      <h1 class="title-block__title">Your Title Goes Here</h1>
      <p class="title-block__subtitle">Your Subtitle Goes Here</p>
    </div>
  </section>

  <!-- blank slide -->
  <section class="slide slide--white" style="top:2402px">
    <div class="ornament ornament--soft" role="img" aria-label="Very faint lotus line ornament"></div>
    <h2 class="slide-heading">Your Blank Slide</h2>
    <div class="brand brand--right"><span class="brand__dot"></span>Laura</div>
    <footer class="footer-band"><span>Yoga Teacher Presentation</span><span class="footer-band__page">7</span></footer>
  </section>

  <!-- three key points -->
  <section class="slide slide--white" style="top:2801px">
    <h2 class="slide-heading">Three Key Point Page</h2>
    <div class="brand brand--right"><span class="brand__dot"></span>Laura</div>
    <div class="feature-band" role="img" aria-label="Teal-toned photo of a person meditating by a lake"></div>
    <div class="feature" style="left:-16px">
      <div class="feature__photo feature__photo--one" role="img" aria-label="Photo of a yoga pose with a glowing energy symbol"></div>
      <h3 class="feature__heading">Heading Here</h3>
      <p class="feature__text">Use this space to explain one key idea in a few short lines so your students can follow along with ease.</p>
    </div>
    <div class="feature" style="left:236px">
      <div class="feature__photo feature__photo--two" role="img" aria-label="Photo of a person meditating at sunset"></div>
      <h3 class="feature__heading">Heading Here</h3>
      <p class="feature__text">Use this space to explain one key idea in a few short lines so your students can follow along with ease.</p>
    </div>
    <div class="feature" style="left:488px">
      <div class="feature__photo feature__photo--three" role="img" aria-label="Photo of a pink lotus flower"></div>
      <h3 class="feature__heading">Heading Here</h3>
      <p class="feature__text">Use this space to explain one key idea in a few short lines so your students can follow along with ease.</p>
    </div>
    <footer class="footer-band"><span>Yoga Teacher Presentation</span><span class="footer-band__page">8</span></footer>
  </section>

  <!-- image left -->
  <section class="slide slide--white" style="top:3199px">
    <h2 class="slide-heading">Image Left</h2>
    <div class="brand brand--right"><span class="brand__dot"></span>Laura</div>
    <div class="photo-left" role="img" aria-label="Photo of a person meditating on a lakeshore at sunrise"></div>
    <ul class="point-list">
      <li class="point-list__item"><span class="point-list__title">Key point title</span> Add a short line of supporting detail here for this idea and keep it brief and clear.</li>
      <li class="point-list__item"><span class="point-list__title">Key point title</span> Add a short line of supporting detail here for this idea and keep it brief and clear.</li>
      <li class="point-list__item"><span class="point-list__title">Key point title</span> Add a short line of supporting detail here for this idea and keep it brief and clear.</li>
    </ul>
    <footer class="footer-band"><span>Yoga Teacher Presentation</span><span class="footer-band__page">9</span></footer>
  </section>

</body>
</html>
```